We need visit card and a letter paper for our website. thx

We have a beauty clinic in Switzerland.
https://wolkenbachtal.ch
We need a visit card.

Requirements
Must have
• see colors on website

```html
<!DOCTYPE html>
<html lang="de">
<head>
<meta charset="utf-8">
<title>Wolkenbachtal – Visitenkarten</title>
<link href="https://fonts.googleapis.com/css2?family=Montserrat:wght@400;500&display=swap" rel="stylesheet">
<style>
  :root {
    --backdrop: #3a3a3c;
    --card: #ebebeb;
    --ink: #222222;
    --accent: #c41a48;
  }
  html, body {
    margin: 0;
    width: 1200px;
    height: 900px;
    overflow: hidden;
    background: var(--backdrop);
    font-family: "Montserrat", sans-serif;
  }
  .card {
    position: absolute;
    width: 510px;
    height: 291px;
    background: var(--card);
    color: var(--ink);
  }
  .card--front-dark { left: 74px; top: 143px; }
  .card--back-logo { left: 616px; top: 143px; }
  .card--front-accent { left: 74px; top: 466px; }
  .card--back-address { left: 616px; top: 466px; }

  .line {
    position: absolute;
    left: 0;
    width: 100%;
    text-align: center;
    margin: 0;
    white-space: nowrap;
    line-height: 18px;
  }
  .brand-name {
    font-size: 32px;
    font-weight: 400;
    letter-spacing: 0.5px;
    line-height: 40px;
  }
  .brand-name--small { font-size: 26px; line-height: 32px; }
  .site-url { font-size: 17px; letter-spacing: 0.6px; line-height: 22px; }
  .card--front-accent .brand-name,
  .card--front-accent .site-url { color: var(--accent); }

  .person-name { font-size: 19px; letter-spacing: 1.5px; text-transform: uppercase; line-height: 22px; }
  .person-role { font-size: 14.5px; color: var(--accent); letter-spacing: 0.6px; }
  .contact { font-size: 14.5px; letter-spacing: 0.6px; }
  .contact .accent { color: var(--accent); }
  .address { font-size: 14px; letter-spacing: 0.6px; line-height: 17px; }

  .dash {
    position: absolute;
    left: 50%;
    width: 13px;
    height: 3px;
    margin-left: -6px;
    background: var(--ink);
  }
  .icon-row {
    position: absolute;
    left: 0;
    width: 100%;
    display: flex;
    justify-content: center;
    gap: 14px;
  }
  .icon-row svg { width: 15px; height: 15px; display: block; }
</style>
</head>
<body>

<section class="card card--front-dark">
  <p class="line brand-name" style="top:113px;">Wolkenbachtal</p>
  <p class="line site-url" style="top:181px;">wolkenbachtal.ch</p>
</section>

<section class="card card--back-logo">
  <p class="line brand-name brand-name--small" style="top:42px;">Wolkenbachtal</p>
  <p class="line person-name" style="top:106px;">Lena Brunner</p>
  <p class="line person-role" style="top:128px;">Doctor of Medicine</p>
  <span class="dash" style="top:157px;"></span>
  <div class="icon-row" style="top:172px;">
    <svg viewBox="0 0 16 16" aria-label="Telefon"><circle cx="8" cy="8" r="8" fill="#c41a48"/><path d="M4.5 9.5h7v2h-7z M5 6.5c2-1.8 4-1.8 6 0v1.5h-1.5v-1h-3v1H5z" fill="#fff"/></svg>
    <svg viewBox="0 0 16 16" aria-label="E-Mail"><circle cx="8" cy="8" r="8" fill="#c41a48"/><rect x="4.3" y="5.3" width="7.4" height="5.4" fill="#fff"/><path d="M4.3 5.3 8 8.3l3.7-3" stroke="#c41a48" stroke-width="0.9" fill="none"/></svg>
    <svg viewBox="0 0 16 16" aria-label="Webseite"><circle cx="8" cy="8" r="8" fill="#c41a48"/><path d="M6 10 10 6 M7.5 5.6l1-1a1.6 1.6 0 0 1 2.3 2.3l-1 1 M8.5 10.4l-1 1a1.6 1.6 0 0 1-2.3-2.3l1-1" stroke="#fff" stroke-width="1.1" fill="none" stroke-linecap="round"/></svg>
  </div>
  <p class="line contact" style="top:197px;">+41 (0) 800 22 30 40</p>
  <p class="line contact" style="top:221px;">hallo@wolkenbachtal.ch</p>
  <p class="line contact" style="top:247px;">www.<span class="accent">wolkenbachtal</span>.ch</p>
</section>

<section class="card card--front-accent">
  <p class="line brand-name" style="top:113px;">Wolkenbachtal</p>
  <p class="line site-url" style="top:181px;">wolkenbachtal.ch</p>
</section>

<section class="card card--back-address">
  <p class="line person-name" style="top:42px;">Lena Brunner</p>
  <p class="line person-role" style="top:64px;">Doctor of Medicine</p>
  <span class="dash" style="top:93px;"></span>
  <div class="icon-row" style="top:108px;">
    <svg viewBox="0 0 16 16" aria-label="Telefon"><circle cx="8" cy="8" r="8" fill="#c41a48"/><path d="M4.5 9.5h7v2h-7z M5 6.5c2-1.8 4-1.8 6 0v1.5h-1.5v-1h-3v1H5z" fill="#fff"/></svg>
    <svg viewBox="0 0 16 16" aria-label="E-Mail"><circle cx="8" cy="8" r="8" fill="#c41a48"/><rect x="4.3" y="5.3" width="7.4" height="5.4" fill="#fff"/><path d="M4.3 5.3 8 8.3l3.7-3" stroke="#c41a48" stroke-width="0.9" fill="none"/></svg>
    <svg viewBox="0 0 16 16" aria-label="Webseite"><circle cx="8" cy="8" r="8" fill="#c41a48"/><path d="M6 10 10 6 M7.5 5.6l1-1a1.6 1.6 0 0 1 2.3 2.3l-1 1 M8.5 10.4l-1 1a1.6 1.6 0 0 1-2.3-2.3l1-1" stroke="#fff" stroke-width="1.1" fill="none" stroke-linecap="round"/></svg>
  </div>
  <p class="line contact" style="top:132px;">+41 (0) 800 22 30 40</p>
  <p class="line contact" style="top:156px;">hallo@wolkenbachtal.ch</p>
  <p class="line contact" style="top:181px;">www.<span class="accent">wolkenbachtal</span>.ch</p>
  <p class="line address" style="top:205px;">Bergweg 14, 7999 Lindenau<br>Switzerland</p>
  <span class="dash" style="top:250px;"></span>
</section>

</body>
</html>
```